Backup Software Tri-fold Brochure Project

We need a great looking and informative brochure to describe our new Backup Software offering. The brochures are to be used in retail and small business environments given to clients interested in protecting their computer from data loss.
The brochure should include attractive imagery that conveys a sense of Trust and Security to the prospective client.
The copy is provided as an attachment to this project. We'd like our Steady Deskframe product logo to be printed on the back cover. The logo is attached to this project.
The finished tri-fold brochure will be submitted to Quellpress for printing as an 8.5" x 11" tri-fold brochure. Their design instructions are online http://quellpress-example.com/custom-brochures.aspx.
The finished product should be Adobe Illustrator CS3 (*.ai) with a PDF Proof.
Target Market(s)
Retail and Small Business customers
Industry/Entity Type
Software
Colors
Designer to choose colors to be used in the design.
Look and feel

```html
<!DOCTYPE html>
<html lang="en">
<head>
<meta charset="utf-8">
<title>Image Backup Tri-fold Brochure – Inside Spread</title>
<link rel="stylesheet" href="https://fonts.googleapis.com/css2?family=Fira+Sans+Condensed:ital,wght@0,400;0,700;1,400;1,700&family=Roboto:ital,wght@0,400;0,700;1,400&display=swap">
<style>
  :root {
    --green: #6b9e44;
    --navy: #2c2e6b;
    --white: #ffffff;
    --paper: #f4f4f6;
    --tile: #d7d7dc;
    --ink: #222226;
    --art-blue: #8fa9d8;
    --art-cream: #e8dcc0;
  }
  * { box-sizing: border-box; margin: 0; padding: 0; }
  html, body { width: 1200px; height: 800px; overflow: hidden; background: #e9e9ec; }
  .spread { position: relative; width: 1200px; height: 800px; display: flex; }
  .panel { position: relative; width: 400px; height: 800px; overflow: hidden; }
  .panel-left { background: var(--paper); padding: 34px 30px; }
  .panel-middle, .panel-right { background: var(--green); }
  .panel-middle { border-right: 1px solid rgba(0,0,0,0.12); border-left: 1px solid rgba(0,0,0,0.08); }
  .panel-heading {
    font-family: "Fira Sans Condensed", sans-serif; font-weight: 700; font-size: 20px;
  }
  .panel-left .panel-heading { color: var(--green); }
  .hero-art {
    margin: 14px 0 22px; width: 340px; height: 270px; border-radius: 6px;
    background: linear-gradient(135deg, var(--art-cream), var(--art-blue) 55%, #cfd6e6);
  }
  .body-copy {
    font-family: "Roboto", sans-serif; font-size: 13px; line-height: 1.38; color: var(--ink);
    text-align: justify; margin-bottom: 14px;
  }
  .task-card {
    position: absolute; left: 20px; top: 28px; width: 360px; height: 300px;
    background: var(--white); border-radius: 30px; padding: 22px 20px 0 18px;
  }
  .task-figure {
    position: absolute; left: 22px; top: 58px; width: 88px; height: 170px; border-radius: 4px;
    background: linear-gradient(180deg, #444, #1d1d1f);
  }
  .task-text { margin-left: 104px; font-family: "Roboto", sans-serif; font-size: 14px; line-height: 1.3; color: var(--ink); }
  .task-card .panel-heading { color: var(--green); margin-left: 104px; margin-bottom: 6px; }
  .task-or { color: var(--green); margin: 6px 0; }
  .task-options { position: absolute; left: 18px; right: 16px; top: 226px; font-family: "Roboto", sans-serif; color: var(--ink); }
  .task-options .lead { font-size: 13.5px; }
  .task-options .lead span { color: var(--green); font-family: "Fira Sans Condensed", sans-serif; font-size: 15px; }
  .task-options li { font-size: 9.5px; list-style: none; margin-top: 4px; }
  .task-options li::before { content: "* "; color: var(--green); }
  .facts { position: absolute; left: 24px; top: 350px; right: 20px; color: var(--white); font-family: "Roboto", sans-serif; }
  .facts .panel-heading { color: var(--navy); font-style: italic; }
  .facts h3 { font-family: "Fira Sans Condensed", sans-serif; font-size: 17px; font-weight: 700; margin: 2px 0 6px; }
  .facts ul { list-style: none; font-size: 13.5px; line-height: 1.35; }
  .facts ul li::before { content: "* "; color: var(--navy); font-weight: 700; }
  .facts h4 { font-family: "Fira Sans Condensed", sans-serif; font-size: 15px; margin: 10px 0 4px; }
  .footnotes { font-size: 11.5px; line-height: 1.35; word-break: break-all; opacity: 0.95; }
  .deco { position: absolute; left: 0; top: 0; pointer-events: none; }
  .how { position: absolute; left: 26px; top: 30px; right: 24px; color: var(--white); }
  .how .panel-heading { color: var(--navy); font-style: italic; margin-bottom: 10px; }
  .how p { font-family: "Roboto", sans-serif; font-style: italic; font-size: 13px; line-height: 1.4; margin-bottom: 14px; }
  .copyright { font-family: "Roboto", sans-serif; font-size: 9px; color: var(--navy); text-align: center; margin-top: 6px; line-height: 1.3; }
</style>
</head>
<body>
<main class="spread">

  <section class="panel panel-left">
    <h2 class="panel-heading">What You Need</h2>
    <div class="hero-art" role="img" aria-label="Illustration of a laptop with a padlock on screen surrounded by security icons, folders and warning signs"></div>
    <p class="body-copy">We can create a snapshot of all the programs and files on your computer using our Image Backup technology. We'll give you your backup on an external hard drive which you can store someplace safe. If anything happens, just bring in your computer and your Image Backup and we'll restore your computer back to the point when the snapshot was taken.</p>
    <p class="body-copy">Restoring from an Image Backup is like setting your computer back in time. To make sure all your new files are protected, we'll also install Brennan-Link's Steady Deskframe software to backup your files every night. These backups are stored in Brennan-Link's secure datacenter to protect you from even the most severe data loss scenarios.</p>
    <p class="body-copy">The combination of your Image Backup and your nightly backup will ensure you have complete protection for both your programs and your files. It means complete peace of mind.</p>
  </section>

  <section class="panel panel-middle">
    <svg class="deco" width="400" height="800" viewBox="0 0 400 800" aria-hidden="true">
      <polygon points="0,630 400,720 400,800 0,800" fill="var(--navy)"/>
      <polygon points="90,690 165,700 150,760 78,748" fill="var(--tile)"/>
      <polygon points="250,690 330,720 305,790 225,760" fill="var(--tile)"/>
      <polygon points="290,650 370,665 355,740 278,722" fill="none" stroke="var(--white)" stroke-width="2"/>
      <polygon points="20,740 80,775 55,800 0,800 0,752" fill="none" stroke="var(--white)" stroke-width="2"/>
    </svg>
    <div class="task-card">
      <div class="task-figure" role="img" aria-label="Silhouette of a businessman standing with arms folded"></div>
      <h2 class="panel-heading">What To Do</h2>
      <div class="task-text">
        <p>Call us to schedule a day to bring in your computer.</p>
        <p class="task-or">OR</p>
        <p>Once a month we do "Image Backup Saturday". Drop off your computer in the morning and pick it up a few hours later. Call for a copy of our schedule.</p>
      </div>
      <div class="task-options">
        <p class="lead"><span>Options</span> : Our Image Backup technology can protect</p>
        <ul>
          <li>Panesys PC's and Laptops running Panesys 7 and above (Panesys 8, 10+)</li>
          <li>Panesys Servers running Panesys 2008 and above (Panesys 2012, 2016+)</li>
        </ul>
      </div>
    </div>
    <div class="facts">
      <h2 class="panel-heading">Did You Know?</h2>
      <h3>Every week (in the US)</h3>
      <ul>
        <li>140,000 drives crash (1)</li>
        <li>12,000 laptops are lost or stolen (2)</li>
        <li>37,000 Internet Crimes are committed (3)</li>
        <li>Internet criminals steal $25 Million (3)</li>
      </ul>
      <h4>Footnotes:</h4>
      <p class="footnotes">(1)http://www.delvar-example.com/downloads/global/services/disk_failures.pdf<br>(2)http://research.searchwell-example.com/archive/lost_laptop_study.pdf<br>(3)https://www.crimewatch-example.gov/media/annualreport/2016_report.pdf</p>
    </div>
  </section>

  <section class="panel panel-right">
    <svg class="deco" width="400" height="800" viewBox="0 0 400 800" aria-hidden="true">
      <polygon points="400,260 400,800 60,800" fill="var(--navy)"/>
      <polygon points="150,470 250,455 262,560 160,575" fill="var(--tile)"/>
      <polygon points="230,400 335,385 350,490 245,505" fill="none" stroke="var(--white)" stroke-width="2"/>
      <polygon points="300,530 390,515 400,600 315,615" fill="var(--tile)"/>
      <polygon points="95,700 190,690 200,780 110,795" fill="var(--tile)"/>
    </svg>
    <div class="how">
      <h2 class="panel-heading">How It Works</h2>
      <p>Our technology is designed to employ powerful imaging technology embedded in Panesys. Deep within the core of the OS is an engine that can create a point-in-time snapshot of the Panesys Operating System, device drivers, programs and system state. The backup can be used later to recover your system back to this point-in-time taken.</p>
      <p>Backups created by our Imaging technology can even be used to restore Panesys to dissimilar hardware. This is a quick way to migrate to a new computer without having to reinstall everything from scratch.</p>
      <p>Our technology stores backups as Halvern Systems "Virtual Hard Disk" (VHD). These VHD files can be directly mounted from the Panesys Disk Manager. This is a great way to browse the contents of your Image Backup and restore individual files and folders.</p>
      <p class="copyright">Copyright(c) 2017, Brennan-Link, Inc.<br>All Rights Reserved</p>
    </div>
  </section>

</main>
</body>
</html>
```